Wedding Decor and Entertianment business card

Company - We run a weddings and events company called Amber Finch, we provide most entertainment and decor services to our customers.

Initial idea is ....
A simple business card with logo on the front, this will be spot varnish. On a matt black background.
The reverse will be simple contact information.

But happy to try things outside of the box and would welcome some crazy ideas.

Target Market(s)

wedding couples - 21 - 40
High end wedding venues.

Industry/Entity Type

Wedding

Contact Information for Business Card

01492 718 263
amberfinchevents.co.uk
rowan@amberfinchevents.co.uk
or
helena@amberfinchevents.co.uk

Requirements
Nice to have
• black matt background with spot varnish logo on the front.

```html
<!DOCTYPE html>
<html lang="en">
<head>
<meta charset="utf-8">
<title>Amber Finch – Business Card</title>
<link rel="stylesheet" href="https://fonts.googleapis.com/css2?family=Jost:wght@400&family=Open+Sans:wght@400;600&display=swap">
<style>
  :root {
    --plum: #7e5577;
    --ink: #2a2a2a;
    --paper: #ffffff;
    --backdrop: #ecebea;
    --card-shadow: 0 10px 30px rgba(0, 0, 0, 0.12);
  }
  * { box-sizing: border-box; margin: 0; padding: 0; }
  html, body {
    width: 1200px;
    height: 900px;
    overflow: hidden;
    background: var(--backdrop);
  }
  .canvas {
    position: relative;
    width: 1200px;
    height: 900px;
  }
  .card {
    position: absolute;
    border-radius: 16px;
    overflow: hidden;
    box-shadow: var(--card-shadow);
  }

  /* Front of card */
  .card-front {
    left: 78px;
    top: 35px;
    width: 588px;
    height: 363px;
    background: var(--paper);
  }
  .card-front .holder {
    position: absolute;
    top: 30px;
    left: 0;
    width: 100%;
    text-align: center;
    font-family: "Open Sans", sans-serif;
    color: var(--ink);
    white-space: nowrap;
  }
  .holder-name {
    font-size: 21px;
    font-weight: 600;
  }
  .holder-name .first { color: var(--plum); }
  .holder-divider {
    display: inline-block;
    width: 2px;
    height: 22px;
    background: var(--ink);
    margin: 0 8px 0 6px;
    vertical-align: -4px;
  }
  .holder-role {
    font-size: 15px;
    font-weight: 400;
  }
  .card-front .band {
    position: absolute;
    top: 84px;
    left: 0;
    width: 100%;
    height: 99px;
    background: var(--plum);
  }
  .card-front .emblem {
    position: absolute;
    left: 233px;
    top: 73px;
    width: 114px;
    height: 114px;
    border-radius: 50%;
    background: var(--paper);
  }
  .wordmark {
    position: absolute;
    left: 0;
    width: 100%;
    text-align: center;
    font-family: "Jost", sans-serif;
    font-weight: 400;
    letter-spacing: 0.28em;
    padding-left: 0.28em;
    white-space: nowrap;
  }
  .card-front .wordmark {
    top: 208px;
    font-size: 28px;
    color: var(--plum);
  }
  .contact {
    position: absolute;
    top: 282px;
    left: 0;
    width: 100%;
    text-align: center;
    font-family: "Open Sans", sans-serif;
    font-size: 15px;
    line-height: 25px;
    color: var(--ink);
  }
  .contact .sep { margin: 0 6px; }

  /* Back of card */
  .card-back {
    left: 390px;
    top: 507px;
    width: 565px;
    height: 348px;
    background: var(--plum);
  }
  .card-back .band {
    position: absolute;
    top: 80px;
    left: 0;
    width: 100%;
    height: 97px;
    background: var(--paper);
  }
  .card-back .emblem {
    position: absolute;
    left: 226px;
    top: 73px;
    width: 112px;
    height: 112px;
    border-radius: 50%;
    background: var(--plum);
  }
  .card-back .wordmark {
    top: 199px;
    font-size: 27px;
    color: var(--paper);
  }
</style>
</head>
<body>
  <main class="canvas">
    <section class="card card-front" aria-label="Business card front">
      <p class="holder">
        <span class="holder-name"><span class="first">Marcus</span> Hale</span><span class="holder-divider"></span><span class="holder-role">Managing Director</span>
      </p>
      <div class="band"></div>
      <div class="emblem"></div>
      <h1 class="wordmark">AMBER FINCH</h1>
      <address class="contact" style="font-style: normal;">
        01492 718 263<span class="sep">|</span>rowan@amberfinchevents.co.uk<br>
        amberfinchevents.co.uk
      </address>
    </section>

    <section class="card card-back" aria-label="Business card back">
      <div class="band"></div>
      <div class="emblem"></div>
      <p class="wordmark">AMBER FINCH</p>
    </section>
  </main>
</body>
</html>
```